Graphic for Webpage

http://www.brightmoorlets.co.uk/market_appraisal.asp

This webpage is selling the fact that we offer a FREE visit by one of our property agents (experts) who can give an estimate of how much your home is worth. The image we currently have is very basic and not very appealing. We are open to a number of issues, one we thought we could utliise is that we have our own agents and could have a few of there photos within the graphic, but we are open to any suggestions. We want it to sync with our site of course.

Property

```html
<!DOCTYPE html>
<html lang="en">
<head>
<meta charset="utf-8">
<title>Brightmoor Lets – Free Market Appraisal</title>
<link rel="stylesheet" href="https://fonts.googleapis.com/css2?family=Open+Sans:wght@300;400;600;700&display=swap">
<style>
  :root{
    --brand-pink:#c81e7a;
    --brand-pink-soft:#d23c8a;
    --brand-green:#8dc63f;
    --brand-olive:#b5b23a;
    --brand-blue:#29aae1;
    --brand-orange:#f7941d;
    --ink:#222;
    --ink-mid:#555;
    --ink-soft:#777;
    --nav-bg:#e2e2e2;
    --header-bg:#f8f8f8;
    --line:#d6d6d6;
    --white:#fff;
  }
  *{box-sizing:border-box;margin:0;padding:0}
  html,body{width:1200px;height:945px;overflow:hidden;background:var(--white)}
  body{position:relative;font-family:"Open Sans",Arial,sans-serif;color:var(--ink)}
  .abs{position:absolute}

  /* contact strip */
  .contact-strip{left:0;top:57px;width:1200px;height:55px;background:var(--brand-pink);color:var(--white)}
  .contact-strip .label{top:20px;font-size:13px;font-weight:400}
  .contact-strip .phone-number{left:264px;top:10px;font-size:28px;font-weight:400;letter-spacing:.3px}
  .social-dot{top:16px;width:25px;height:25px;border-radius:5px;background:rgba(255,255,255,.35)}
  .search-box{left:1057px;top:15px;width:160px;height:30px;border-radius:15px;background:var(--white);
    color:#8a8a8a;font-weight:700;font-size:15px;padding:5px 10px;white-space:nowrap;overflow:hidden}

  /* header */
  .site-header{left:0;top:112px;width:1200px;height:121px;background:var(--header-bg)}
  .brand{left:80px;top:34px;display:flex;align-items:center;gap:14px}
  .brand-mark{width:44px;height:44px;background:var(--brand-pink)}
  .brand-name{font-size:30px;font-weight:600;color:#5b5b5b;letter-spacing:.5px;white-space:nowrap}
  .service-tab{top:28px;height:24px;font-size:12px;line-height:24px;padding:0 5px;white-space:nowrap}
  .service-tab.active{background:var(--brand-pink);color:var(--white)}
  .tagline{left:768px;top:69px;font-size:24px;color:var(--brand-pink);white-space:nowrap}

  /* main navigation */
  .main-nav{left:0;top:233px;width:1200px;height:35px;background:var(--nav-bg)}
  .nav-item{top:9px;font-size:14px;color:#333;white-space:nowrap}
  .nav-sep{top:7px;width:2px;height:21px}

  /* appraisal intro */
  .page-title{left:77px;top:298px;font-size:39px;font-weight:300;color:#111}
  .title-rule{left:77px;top:365px;width:372px;height:4px;background:var(--brand-pink)}
  .agent-photo{left:70px;top:385px;width:520px;height:345px;
    background:radial-gradient(ellipse at 60% 50%,#c9c4c8 0%,#e8e6ea 40%,#fafafa 75%,#fff 100%)}
  .benefits{left:70px;top:631px;width:210px;list-style:none}
  .benefits li{display:flex;justify-content:flex-end;align-items:center;gap:10px;height:26.5px;font-size:16px;color:#111}
  .tick{width:14px;height:14px}

  .intro-copy{left:677px;top:380px;width:523px;overflow:hidden}
  .intro-copy h2{font-size:20px;font-weight:400;color:var(--brand-pink);margin-bottom:12px;white-space:nowrap}
  .intro-copy p{font-size:14px;line-height:24px;color:var(--ink-soft);white-space:nowrap;margin-bottom:24px}

  .section-rule{left:120px;top:771px;width:1080px;height:2px;
    background:linear-gradient(to right,rgba(0,0,0,0),#e6e6e6 15%,#e6e6e6 85%,rgba(0,0,0,0))}

  /* booking form */
  .form-title{left:107px;top:823px;font-size:20px;font-weight:400;color:var(--brand-pink)}
  .form-note{left:107px;top:865px;font-size:14px;font-weight:700;color:var(--ink-mid)}
  .field{top:906px;width:270px}
  .field label{display:block;font-size:14px;color:var(--ink-mid);margin-bottom:8px}
  .field .input{height:40px;border:1px solid #cfcfcf;border-radius:4px;background:var(--white)}
</style>
</head>
<body>

<div class="abs contact-strip">
  <span class="abs label" style="left:78px">Get in touch!</span>
  <svg class="abs" style="left:164px;top:22px" width="11" height="11" viewBox="0 0 24 24" aria-hidden="true">
    <path fill="#fff" d="M6.6 10.8a15.1 15.1 0 0 0 6.6 6.6l2.2-2.2c.3-.3.7-.4 1-.2 1.1.4 2.3.6 3.6.6.6 0 1 .4 1 1V20c0 .6-.4 1-1 1A17 17 0 0 1 3 4c0-.6.4-1 1-1h3.5c.6 0 1 .4 1 1 0 1.3.2 2.5.6 3.6.1.3 0 .7-.2 1z"/>
  </svg>
  <span class="abs label" style="left:181px">FREEPHONE</span>
  <span class="abs phone-number">0808 196 0342</span>
  <span class="abs label" style="left:470px">Open today for Calls: 9am-8pm</span>
  <span class="abs social-dot" style="left:684px"></span>
  <span class="abs social-dot" style="left:714px"></span>
  <span class="abs social-dot" style="left:746px"></span>
  <div class="abs search-box">Search Our Homes</div>
</div>

<header class="abs site-header">
  <div class="abs brand">
    <span class="brand-mark"></span>
    <span class="brand-name">BRIGHTMOOR LETS</span>
  </div>
  <span class="abs service-tab active" style="left:915px">SALES</span>
  <span class="abs service-tab" style="left:969px;color:var(--brand-olive)">LETTINGS</span>
  <span class="abs service-tab" style="left:1043px;color:var(--brand-blue)">CONVEYANCING</span>
  <span class="abs service-tab" style="left:1155px;color:var(--brand-orange)">MORTGAGES</span>
  <span class="abs tagline">The UK's Biggest &amp; Best Online Estate Agent</span>
</header>

<nav class="abs main-nav">
  <span class="abs nav-item" style="left:101px">HOME</span>
  <span class="abs nav-sep" style="left:171px;background:var(--brand-pink)"></span>
  <span class="abs nav-item" style="left:202px">FEES</span>
  <span class="abs nav-sep" style="left:260px;background:var(--brand-olive)"></span>
  <span class="abs nav-item" style="left:291px">INSTRUCT US</span>
  <span class="abs nav-sep" style="left:406px;background:var(--brand-blue)"></span>
  <span class="abs nav-item" style="left:437px">WHY US</span>
  <span class="abs nav-sep" style="left:518px;background:var(--brand-orange)"></span>
  <span class="abs nav-item" style="left:548px">TESTIMONIALS</span>
  <span class="abs nav-sep" style="left:673px;background:var(--brand-pink)"></span>
  <span class="abs nav-item" style="left:704px">HOW IT WORKS</span>
  <span class="abs nav-sep" style="left:834px;background:var(--brand-olive)"></span>
  <span class="abs nav-item" style="left:865px">FREE VALUATION</span>
  <span class="abs nav-sep" style="left:1005px;background:var(--brand-blue)"></span>
  <span class="abs nav-item" style="left:1035px">CONTACT</span>
  <span class="abs nav-sep" style="left:1127px;background:var(--brand-orange)"></span>
  <span class="abs nav-item" style="left:1158px">LOGIN</span>
</nav>

<h1 class="abs page-title">FREE Market Appraisal</h1>
<div class="abs title-rule"></div>

<div class="abs agent-photo" role="img" aria-label="Property consultant showing a folder to a couple in a bright, empty room"></div>

<ul class="abs benefits">
  <li>Access the property
    <svg class="tick" viewBox="0 0 14 14" aria-hidden="true"><circle cx="7" cy="7" r="7" fill="var(--brand-pink-soft)"/><path d="M3.8 7.2l2.2 2.1 4.2-4.4" fill="none" stroke="#fff" stroke-width="1.8"/></svg></li>
  <li>Estimate Value
    <svg class="tick" viewBox="0 0 14 14" aria-hidden="true"><circle cx="7" cy="7" r="7" fill="var(--brand-blue)"/><path d="M3.8 7.2l2.2 2.1 4.2-4.4" fill="none" stroke="#fff" stroke-width="1.8"/></svg></li>
  <li>Best Price Tactics
    <svg class="tick" viewBox="0 0 14 14" aria-hidden="true"><circle cx="7" cy="7" r="7" fill="var(--brand-orange)"/><path d="M3.8 7.2l2.2 2.1 4.2-4.4" fill="none" stroke="#fff" stroke-width="1.8"/></svg></li>
  <li>Answer Questions
    <svg class="tick" viewBox="0 0 14 14" aria-hidden="true"><circle cx="7" cy="7" r="7" fill="var(--brand-green)"/><path d="M3.8 7.2l2.2 2.1 4.2-4.4" fill="none" stroke="#fff" stroke-width="1.8"/></svg></li>
</ul>

<section class="abs intro-copy">
  <h2>Be in control of your marketing price !</h2>
  <p>As the UK's Biggest and most successful fixed fee estate agent, we have our own<br>employed network of property consultants who offer face to face market appraisals.</p>
  <p>Our agent will assess your property, estimate the valuation, discuss tactics to achieve<br>the very best sale price and answer any questions you have.</p>
  <p>In our view any agent that is not prepared to visit you before being instructed cannot<br>be trusted to offer a high level personal service.</p>
  <p>If you already know the price you want to market your home for, you can instruct us<br>without an appraisal as this enables a much quicker marketing turn around. If you are<br>still unsure and would like to meet our consultant, please complete the form below.</p>
</section>

<div class="abs section-rule"></div>

<h2 class="abs form-title">Book a FREE No Obligation Market Appraisal</h2>
<p class="abs form-note">We offer a two stage market appraisal and conduct an initial telephone consultation, followed by our home visit.</p>

<div class="abs field" style="left:107px"><label>First Name</label><div class="input"></div></div>
<div class="abs field" style="left:407px"><label>Last Name</label><div class="input"></div></div>
<div class="abs field" style="left:707px"><label>Your email address</label><div class="input"></div></div>
<div class="abs field" style="left:1007px"><label>Landline</label><div class="input"></div></div>

</body>
</html>
```